Varro's Electrical & Solar Corflute Signage Design

So my plan is to put this design onto a 600 by 400 corflute sign (this sign will be printed out and cable tied to a fence FYI). I would like to have the name and the icon stand out. I need Varro's Electrical & Solar to be big and clear and I would like to have my "S" icon faded behind "Varro's Electrical & Solar" in the background.

I want to have my Lic No. - Top left with my ABN directly underneath. (I Want two ticks infront of them like this)
✓ Lic No. 582164K
✓ ABN 41 276 519 683

I want to have written on it: ALL ASPECTS OF ELECTRICAL (please use cool fonts and nothing too plain)
I also want to have: YOUR LOCAL TRUSTED ELECTRICIAN but if it looks too dicky then just have "all aspects of electrical" and just "free quotes • fast service" somewhere.
Directly underneath (smaller but still clear): FREE QUOTES • FAST SERVICE

At the bottom, I need my phone number big and clear - 0438 617 905 I would like this on a banner meaning like a cool strip at the bottom. (Please make the strip/banner look cool and not boring. Maybe shade the colour or something)
I also want the Facebook & Instagram icons on there so people can look us up on facebook & Instagram (make them match the colour of my logo or you could try any other colour that works)
Thank you so much!!

Colors

Designer to choose colors to be used in the design.

Requirements
Should not have
• no different colours other then the colours on my logo and icon

```html
<!DOCTYPE html>
<html lang="en">
<head>
<meta charset="utf-8">
<title>Varro's Electrical &amp; Solar – Fence Sign</title>
<link href="https://fonts.googleapis.com/css2?family=Montserrat:wght@400;800&family=Poppins:wght@500;600;700;800&display=swap" rel="stylesheet">
<style>
  :root{
    --backdrop:#2a2a2a;
    --sign-black:#050607;
    --sign-charcoal:#17191b;
    --silver:#d1d2d4;
    --white:#ffffff;
    --green-dark:#1f9a48;
    --green:#3db54a;
    --green-light:#7cc96a;
    --ink:#000000;
  }
  *{margin:0;padding:0;box-sizing:border-box}
  html,body{width:860px;height:1200px;overflow:hidden;background:var(--backdrop)}
  .sign{
    position:absolute;left:30px;top:0;width:800px;height:1200px;overflow:hidden;
    background:var(--sign-black);
    font-family:'Poppins',sans-serif;
  }
  .sign__texture{
    position:absolute;left:0;top:0;width:800px;height:966px;
    background:radial-gradient(ellipse at 50% 40%,var(--sign-charcoal) 0%,var(--sign-black) 75%);
  }
  .credentials{
    position:absolute;left:57px;top:44px;color:var(--white);
    font-size:31px;line-height:37px;font-weight:500;letter-spacing:-.3px;
  }
  .credentials b{font-weight:700}
  .brand__ring{
    position:absolute;left:281px;top:163px;width:236px;height:236px;border-radius:50%;
    border:10px solid rgba(209,210,212,.08);
  }
  .brand{
    position:absolute;left:0;width:800px;text-align:center;top:228px;
  }
  .brand__name{
    display:block;color:var(--green);font-weight:800;font-size:112px;line-height:100px;letter-spacing:-2px;
  }
  .brand__tag{
    display:block;margin-top:6px;color:var(--silver);font-weight:700;font-size:22px;letter-spacing:9px;
  }
  .headline{position:absolute;left:0;width:800px;text-align:center;white-space:nowrap}
  .headline--all{top:443px;font-size:100px;line-height:100px;color:var(--silver);font-weight:500;letter-spacing:-3px}
  .headline--aspects{top:547px;font-size:100px;line-height:100px;color:var(--silver);font-weight:500;letter-spacing:-3px}
  .headline--electrical{
    top:647px;font-size:120px;line-height:120px;font-weight:700;letter-spacing:-3px;
    background:linear-gradient(90deg,var(--green-dark),var(--green-light) 50%,var(--green));
    -webkit-background-clip:text;background-clip:text;color:transparent;
  }
  .divider{
    position:absolute;left:0;top:795px;width:800px;height:2px;
    background:linear-gradient(90deg,transparent,rgba(209,210,212,.35) 50%,transparent);
  }
  .offer{
    position:absolute;left:0;top:815px;width:800px;text-align:center;white-space:nowrap;
    color:var(--silver);font-weight:600;font-size:47px;line-height:56px;letter-spacing:.5px;
  }
  .offer__dot{
    display:inline-block;width:18px;height:18px;border-radius:50%;background:var(--green);
    vertical-align:middle;margin:0 14px 8px;
  }
  .phone-band{
    position:absolute;left:0;top:966px;width:800px;height:119px;
    background:linear-gradient(90deg,var(--green-dark) 0%,var(--green) 28%,var(--green-light) 50%,var(--green) 75%,var(--green-dark) 100%);
  }
  .phone-band__icon{position:absolute;left:56px;top:24px;width:72px;height:72px}
  .phone-band__number{
    position:absolute;left:146px;top:14px;font-family:'Montserrat',sans-serif;font-weight:800;
    font-size:86px;line-height:90px;color:var(--ink);letter-spacing:-2px;white-space:nowrap;
  }
  .social{
    position:absolute;left:0;top:1112px;width:800px;text-align:center;white-space:nowrap;
    font-family:'Montserrat',sans-serif;font-size:33px;line-height:44px;color:var(--white);
  }
  .social__dot{
    display:inline-block;width:28px;height:28px;border-radius:50%;background:var(--green);
    vertical-align:middle;margin:0 10px 6px 0;
  }
</style>
</head>
<body>
<main class="sign">
  <div class="sign__texture" role="img" aria-label="Dark charcoal background texture"></div>

  <div class="credentials">
    <div>Lic No. <b>582164K</b></div>
    <div>ABN <b>41 276 519 683</b></div>
  </div>

  <div class="brand__ring"></div>
  <div class="brand">
    <span class="brand__name">VARRO'S</span>
    <span class="brand__tag">ELECTRICAL &amp; SOLAR</span>
  </div>

  <div class="headline headline--all">ALL</div>
  <div class="headline headline--aspects">ASPECTS OF</div>
  <div class="headline headline--electrical">ELECTRICAL</div>

  <div class="divider"></div>
  <div class="offer">FREE QUOTES<span class="offer__dot"></span>FAST SERVICE</div>

  <div class="phone-band">
    <svg class="phone-band__icon" viewBox="0 0 72 72" aria-hidden="true">
      <circle cx="36" cy="36" r="36" fill="#000"/>
      <path d="M24 18c3 0 6 7 6 9s-3 3-3 5c1 4 6 9 10 10 2 0 3-3 5-3s9 3 9 6c0 3-4 7-8 7-12 0-25-13-25-25 0-4 3-9 6-9z" fill="#3db54a"/>
      <path d="M40 22a11 11 0 0 1 10 10M40 15a18 18 0 0 1 17 17" stroke="#3db54a" stroke-width="3.5" fill="none" stroke-linecap="round"/>
    </svg>
    <div class="phone-band__number">0438 617 905</div>
  </div>

  <div class="social"><span class="social__dot"></span>@varros_electrical</div>
</main>
</body>
</html>
```